Creative Consulting Company
business card, stationary, ppt template
Creative Consulting Company - Communications and Media
Creative Brief
Use specific fonts
Use what works the best in your design
Professional
Till Molnar
CEO
Molnar Communications GmbH Tannwaldstrasse 87 CH-8999 Zurich
till.molnar@molnarkom-demo.ch
www.molnarkom-demo.ch
Molnar Communications is a consultancy that specializes in all aspects of high end event organization and sponsorship activation. We are located in Switzerland. I'm looking for a clean and stylish look. The sizes are european: Letterhead: DIN A4 210mm x 297mm (8.27" x 11.69") Business Cards: 85mm x 54mm (3.346" x 2.126") Plz use "Mobile" instead of "Cell" Stationery: --------------- Do not use Ilustration which runs off the edge. We do print the letters with our own printers. Therefore, there will be a margin. And please no watermarks. Business Cards: ----------------------- I consider to grade up the back of the card with some varnish or film, but not sure yet. You can use either the black or the white logo. ppt Template: ------------------ Template should match the grafical concept.
Just the Logo. I you mind pimp up the logo a little bit (gradient, shadow, 3D etc.), feel free to do so. But you don't have to.

```html
<!DOCTYPE html>
<html lang="en">
<head>
<meta charset="utf-8">
<title>Molnar Communications – Stationery</title>
<link href="https://fonts.googleapis.com/css2?family=Montserrat:wght@400;600&display=swap" rel="stylesheet">
<style>
  :root {
    --bg: #e6e6e6;
    --paper: #ffffff;
    --ink: #3f3f3f;
    --ink-soft: #7a7a7a;
    --band-dark: #4d4d4d;
    --band-light: #8c8c8c;
    --shadow: 0 3px 10px rgba(0,0,0,.18);
  }
  * { box-sizing: border-box; margin: 0; padding: 0; }
  html, body { width: 1200px; height: 887px; overflow: hidden; }
  body { background: var(--bg); font-family: "Montserrat", sans-serif; color: var(--ink); position: relative; }

  .piece { position: absolute; background: var(--paper); box-shadow: var(--shadow); overflow: hidden; }

  /* wordmark: plain dot beside the company name, one weight, one colour */
  .brand { display: inline-flex; align-items: center; gap: 8px; color: var(--ink); white-space: nowrap; }
  .brand .dot { width: 10px; height: 10px; border-radius: 50%; background: currentColor; flex: none; }
  .brand .name { font-weight: 600; font-size: 18px; line-height: 1; }
  .brand.small { gap: 6px; }
  .brand.small .dot { width: 7px; height: 7px; }
  .brand.small .name { font-size: 12px; }
  .brand.light { color: var(--paper); }

  .center { position: absolute; left: 0; right: 0; display: flex; justify-content: center; }

  /* envelope back */
  .envelope-back { left: 60px; top: 70px; width: 340px; height: 210px; }
  .envelope-back svg { position: absolute; inset: 0; }
  .envelope-back .top { top: 34px; }
  .envelope-back .flap { top: 120px; }

  /* letterhead */
  .letterhead { left: 440px; top: 36px; width: 356px; height: 503px; }
  .letterhead .head { top: 58px; }
  .letterhead .footer { position: absolute; left: 0; right: 0; bottom: 20px; text-align: center; font-size: 6.5px; line-height: 1.6; color: var(--ink); }
  .letterhead .footer b { font-weight: 600; }

  /* envelope front (DL) */
  .envelope-front { left: 60px; top: 560px; width: 480px; height: 240px; }
  .envelope-front .brand { position: absolute; left: 30px; top: 42px; }
  .envelope-front .sender { position: absolute; left: 30px; top: 128px; font-size: 6.5px; line-height: 1.6; color: var(--ink-soft); }
  .envelope-front .edge { position: absolute; left: 0; right: 0; bottom: 0; height: 8px; background: linear-gradient(90deg, var(--band-dark), var(--band-light)); }

  /* business cards */
  .card { width: 250px; height: 159px; left: 880px; }
  .card-logo { top: 60px; display: flex; align-items: center; justify-content: center; }
  .card-back { top: 250px; background: linear-gradient(135deg, var(--band-dark), var(--band-light)); display: flex; align-items: center; justify-content: center; }
  .card-back .url { position: absolute; bottom: 14px; left: 0; right: 0; text-align: center; font-size: 6.5px; letter-spacing: .08em; color: var(--paper); }
  .card-contact { top: 440px; }
  .card-contact .brand { position: absolute; left: 18px; top: 22px; }
  .card-contact .person { position: absolute; right: 20px; top: 46px; font-size: 8px; font-weight: 600; text-align: right; }
  .card-contact .person span { display: block; font-weight: 400; font-size: 6px; color: var(--ink-soft); margin-top: 2px; }
  .card-contact .details { position: absolute; left: 18px; top: 92px; font-size: 5.5px; line-height: 1.65; color: var(--ink); }
  .card-contact .edge { position: absolute; left: 0; right: 0; bottom: 0; height: 6px; background: linear-gradient(90deg, var(--band-dark), var(--band-light)); }
</style>
</head>
<body>

  <section class="piece envelope-back" aria-label="Envelope back">
    <svg width="340" height="210" viewBox="0 0 340 210">
      <defs>
        <linearGradient id="flapTone" x1="0" y1="0" x2="1" y2="1">
          <stop offset="0" stop-color="#4d4d4d"/>
          <stop offset="1" stop-color="#8c8c8c"/>
        </linearGradient>
      </defs>
      <polygon points="0,82 340,82 340,104 210,178 130,178 0,104" fill="url(#flapTone)"/>
    </svg>
    <div class="center top"><div class="brand small"><span class="dot"></span><span class="name">Molnar Communications</span></div></div>
    <div class="center flap"><div class="brand small light"><span class="dot"></span><span class="name">Molnar Communications</span></div></div>
  </section>

  <section class="piece letterhead" aria-label="Letterhead">
    <div class="center head"><div class="brand"><span class="dot"></span><span class="name">Molnar Communications</span></div></div>
    <p class="footer">
      Molnar Communications GmbH Tannwaldstrasse 87 CH-8999 Zurich<br>
      <b>Mobile:</b> +41 79 555 01 23 | <b>Email:</b> till.molnar@molnarkom-demo.ch | www.molnarkom-demo.ch
    </p>
  </section>

  <section class="piece envelope-front" aria-label="Envelope front">
    <div class="brand"><span class="dot"></span><span class="name">Molnar Communications</span></div>
    <p class="sender">Molnar Communications GmbH<br>Tannwaldstrasse 87 CH-8999 Zurich</p>
    <div class="edge"></div>
  </section>

  <section class="piece card card-logo" aria-label="Business card front">
    <div class="brand small"><span class="dot"></span><span class="name">Molnar Communications</span></div>
  </section>

  <section class="piece card card-back" aria-label="Business card back">
    <div class="brand small light"><span class="dot"></span><span class="name">Molnar Communications</span></div>
    <p class="url">www.molnarkom-demo.ch</p>
  </section>

  <section class="piece card card-contact" aria-label="Business card contact side">
    <div class="brand small"><span class="dot"></span><span class="name">Molnar Communications</span></div>
    <p class="person">Till Molnar<span>CEO</span></p>
    <p class="details">
      Molnar Communications GmbH<br>
      Tannwaldstrasse 87 CH-8999 Zurich<br>
      Mobile +41 79 555 01 23<br>
      till.molnar@molnarkom-demo.ch
    </p>
    <div class="edge"></div>
  </section>

</body>
</html>
```